STOREFRONT SIGNAGE/ NEW LOGO

Looking for someone to enhance my current sign idea. I own a pawn shop , which is also a gun shop. I want a catchy front sign, which will be a lighted box sign. I may want to incorporate some symbols or character symbology that highlight firearms, such as : guns, ammo, targets, scope retical , gold, diamonds, cash, watches and/or pawn balls, and im open to other ideas, but i do not want it too busy, i want it simple, with a twist. Attached, you will find a very basic design, showing the business name and the verbiage that I would like to be incorporated into the design. God bless and thank you. may the best design win !

```html
<!DOCTYPE html>
<html lang="en">
<head>
<meta charset="utf-8">
<title>Meridian Gold Exchange &amp; Gun Exchange – Storefront Sign</title>
<link rel="stylesheet" href="https://fonts.googleapis.com/css2?family=Poppins:ital,wght@0,600;0,700;1,800&display=swap">
<style>
  :root {
    --backdrop: #eeeeee;
    --sign-white: #ffffff;
    --sign-red: #ec1c24;
    --gold: #d4a32f;
    --ink: #0a0a0a;
    --divider: #1a1a1a;
  }
  html, body {
    margin: 0;
    padding: 0;
    width: 1200px;
    height: 1200px;
    overflow: hidden;
    background: var(--backdrop);
    font-family: "Poppins", Arial, sans-serif;
  }
  .canvas {
    position: relative;
    width: 1200px;
    height: 1200px;
  }
  .sign {
    position: absolute;
    left: 92px;
    top: 480px;
    width: 1016px;
    height: 241px;
    background: var(--sign-white);
    box-shadow: 0 2px 6px rgba(0,0,0,0.18);
  }
  .sign__main {
    position: absolute;
    left: 0;
    top: 0;
    width: 794px;
    height: 172px;
    border-right: 3px solid var(--divider);
    border-bottom: 3px solid var(--divider);
  }
  .headline-word {
    position: absolute;
    margin: 0;
    font-weight: 700;
    line-height: 1;
    white-space: nowrap;
    transform: translateX(-50%);
  }
  .headline-word--gold { color: var(--gold); }
  .headline-word--gun { color: var(--ink); }
  .headline-word--top { top: 24px; font-size: 56px; }
  .headline-word--bottom { top: 95px; font-size: 57px; }
  .gold-top { left: 178px; }
  .gold-bottom { left: 178px; }
  .gun-top { left: 615px; }
  .gun-bottom { left: 616px; }

  .brand-tag {
    position: absolute;
    left: 305px;
    top: 24px;
    width: 184px;
    height: 54px;
    display: flex;
    align-items: center;
    justify-content: center;
    gap: 10px;
  }
  .brand-tag__mark {
    width: 14px;
    height: 14px;
    background: var(--gold);
  }
  .brand-tag__name {
    font-size: 24px;
    font-weight: 600;
    color: var(--ink);
    letter-spacing: 1px;
    line-height: 1;
  }
  .ampersand {
    position: absolute;
    left: 358px;
    top: 93px;
    width: 78px;
    height: 78px;
    border-radius: 50%;
    background: var(--sign-red);
    color: var(--sign-white);
    font-size: 50px;
    font-weight: 700;
    display: flex;
    align-items: center;
    justify-content: center;
    line-height: 1;
  }
  .ampersand span { transform: translateY(3px); }

  .tagline-band {
    position: absolute;
    left: 0;
    top: 182px;
    width: 797px;
    height: 59px;
    background: var(--sign-red);
    display: flex;
    align-items: center;
    justify-content: center;
  }
  .tagline {
    margin: 0;
    color: var(--sign-white);
    font-size: 38px;
    font-weight: 800;
    font-style: italic;
    line-height: 1;
    white-space: nowrap;
  }

  .services-panel {
    position: absolute;
    left: 801px;
    top: 0;
    width: 215px;
    height: 241px;
    background: var(--sign-red);
  }
  .services {
    list-style: none;
    margin: 0;
    padding: 0;
    position: absolute;
    left: 32px;
    top: 30px;
  }
  .services li {
    color: var(--sign-white);
    font-size: 24px;
    font-weight: 600;
    line-height: 37.5px;
    letter-spacing: 0.5px;
  }
  .services li::before {
    content: "•";
    margin-right: 8px;
  }
</style>
</head>
<body>
<div class="canvas">
  <section class="sign" aria-label="Meridian Gold Exchange and Gun Exchange storefront sign">
    <div class="sign__main">
      <span class="headline-word headline-word--gold headline-word--top gold-top">GOLD</span>
      <span class="headline-word headline-word--gold headline-word--bottom gold-bottom">Exchange</span>
      <div class="brand-tag">
        <span class="brand-tag__mark"></span>
        <span class="brand-tag__name">MERIDIAN</span>
      </div>
      <div class="ampersand"><span>&amp;</span></div>
      <span class="headline-word headline-word--gun headline-word--top gun-top">GUN</span>
      <span class="headline-word headline-word--gun headline-word--bottom gun-bottom">Exchange</span>
    </div>
    <div class="tagline-band">
      <p class="tagline">CASH FOR GOLD .......CASH FOR GUNS</p>
    </div>
    <aside class="services-panel">
      <ul class="services">
        <li>PAWN</li>
        <li>BUY</li>
        <li>SELL</li>
        <li>TRADE</li>
        <li>LAYAWAY</li>
      </ul>
    </aside>
  </section>
</div>
</body>
</html>
```